Ice Cream Container Print Design

This is an ice cream cup. This is for a homemade raspberry ice cream. I need it to be eye catching, pops from the shelf, with a gourmet look as well. I am looking for more of the Velmont Creme Ice cream type of style with it being elegant but also fun.

This goes into grocery shelves in the freezer. It has a clear lid so that is not included. The design sheet is for the space that wraps around the cup.

Target Market(s)

Grocery freezer shelves

Industry/Entity Type

Food Production

Font styles to use
Serif
Script

Colors
ec1f27
ffc214

Requirements
Must have
• Orvin's Logo and Fox Hollow. Please also use the berry cluster. I would like reds, golds, and blacks. I want a background design or color.
• I want it to say "Homemade Raspberry Ice Cream"
Nice to have
• As the spec sheet indicates on the bottom left, please make the front repeat 2 times as is goes around the cup.
Should not have
• Please do not make it look like a clown show. I want it fun and gourmet looking.

```html
<!DOCTYPE html>
<html lang="en">
<head>
<meta charset="utf-8">
<title>Orvin's Fox Hollow – Homemade Raspberry Ice Cream Cup Wrap</title>
<link rel="stylesheet" href="https://fonts.googleapis.com/css2?family=Playfair+Display:wght@700&family=Noto+Sans+Mono:wght@500;700&display=swap">
<style>
  :root {
    --page: #ffffff;
    --label-cream: #fbf8f3;
    --swirl-tone: #efe3cf;
    --gold: #c28a17;
    --ink: #1e1e1e;
    --berry-red: #c42235;
    --drip-red: #d41f36;
    --berry-light: #f07a90;
    --berry-deep: #b81f3c;
  }
  html, body {
    margin: 0;
    width: 1200px;
    height: 1083px;
    overflow: hidden;
    background: var(--page);
  }
  .canvas {
    position: relative;
    width: 1200px;
    height: 1083px;
  }
  .cup-wrap {
    position: absolute;
    left: 80px;
    top: 116px;
    width: 1040px;
    height: 850px;
    overflow: hidden;
    background: var(--label-cream);
  }
  .swirl-background {
    position: absolute;
    inset: 0;
    width: 100%;
    height: 100%;
  }
  .brand {
    position: absolute;
    left: 70px;
    top: 100px;
    width: 500px;
    font-family: "Playfair Display", Georgia, serif;
    font-weight: 700;
    color: var(--gold);
  }
  .brand-name {
    display: block;
    font-size: 150px;
    line-height: 1;
  }
  .brand-place {
    display: block;
    font-size: 62px;
    line-height: 1;
    text-align: right;
    margin-top: 6px;
  }
  .flavour {
    margin: 0;
    font-family: "Noto Sans Mono", "Courier New", monospace;
    font-weight: 500;
    color: var(--ink);
  }
  .flavour span {
    position: absolute;
    left: 104px;
    line-height: 1;
    white-space: nowrap;
  }
  .flavour-top { top: 462px; font-size: 58px; letter-spacing: 3px; }
  .flavour-name {
    top: 538px;
    font-size: 74px;
    font-weight: 700;
    letter-spacing: 2px;
    color: var(--berry-red);
  }
  .flavour-bottom { top: 624px; font-size: 58px; letter-spacing: 3px; }
  .berry-cluster {
    position: absolute;
    left: 605px;
    top: 285px;
    width: 420px;
    height: 360px;
    border-radius: 50%;
    background: radial-gradient(ellipse at 50% 50%, var(--berry-light) 0%, rgba(228, 84, 112, 0.85) 45%, rgba(210, 60, 90, 0.25) 70%, rgba(251, 248, 243, 0) 72%);
  }
  .drip-band {
    position: absolute;
    left: 0;
    bottom: 0;
    width: 100%;
    height: 170px;
  }
  .drip-band path { fill: var(--drip-red); }
</style>
</head>
<body>
  <main class="canvas">
    <section class="cup-wrap">
      <svg class="swirl-background" role="img" aria-label="Soft cream background with fine golden swirl pattern" viewBox="0 0 1040 850" preserveAspectRatio="none">
        <defs>
          <radialGradient id="swirlTone" cx="0.45" cy="0.4" r="0.8">
            <stop offset="0" stop-color="#fbf8f3"/>
            <stop offset="1" stop-color="#efe3cf"/>
          </radialGradient>
        </defs>
        <rect width="1040" height="850" fill="url(#swirlTone)"/>
      </svg>

      <div class="brand">
        <span class="brand-name">Orvin's</span>
        <span class="brand-place">Fox Hollow</span>
      </div>

      <h1 class="flavour">
        <span class="flavour-top">Homemade</span>
        <span class="flavour-name">RASPBERRY</span>
        <span class="flavour-bottom">Ice Cream</span>
      </h1>

      <div class="berry-cluster" role="img" aria-label="Cluster of three ripe raspberries with green leaves"></div>

      <svg class="drip-band" viewBox="0 0 1040 170" preserveAspectRatio="none" aria-hidden="true">
        <path d="M0,170 L0,58 L11,58 C11,6 179,6 179,58 L325,58 C325,6 482,6 482,58 L549,58 C549,0 728,0 728,58 L795,58 C795,6 952,6 952,58 L963,58 C963,10 1040,10 1040,40 L1040,170 Z"/>
      </svg>
    </section>
  </main>
</body>
</html>
```